The Amber Tides (celtic rap album by Oskar Venlow)

Peace. I'm Oskar Venlow, I make celtic/druidic/pagan rap music. The album is called ' The Amber Tides ' which has to do with celtic cosmology: The Underworld (The Sea) is the realms of the past, the ancestors, trauma, transformation, knowledge of the old ways ... ; This World (The Land) is the realm of ordinary reality, our life, the present, skills, fertility ... ; and The Upperworld (The Sky) which is the realm of the gods, the future, goals, planning of harvest.... Three was a sacred number and describes the fullness of life and is symbolized by the triskele, e.g. found at Dunmorrow.

I have no idea for a cover lol, so go wild. It would be good if the three worlds are somehow featured.

This is one of the songs: https://www.clipvault-example.net/watch?v=qRtLmnWXpZA

Target Market(s)

pagans, spiritual people

Requirements
Must have
• something that references The Amber Tides (see description)
Nice to have
• Celtic symbol(s); contrasts between light and dark; past - present - future

```html
<!DOCTYPE html>
<html lang="en">
<head>
<meta charset="utf-8">
<title>The Amber Tides — Oskar Venlow</title>
<link rel="stylesheet" href="https://fonts.googleapis.com/css2?family=Uncial+Antiqua&family=Josefin+Sans:wght@600&display=swap">
<style>
  :root {
    --sun: #fff3a6;
    --amber: #f7a640;
    --ember: #c8563a;
    --dusk: #6b2f55;
    --night: #261a3c;
    --stone: #6e5a4c;
    --shore: #c9b27a;
    --sea-light: #8fc3c7;
    --sea: #2e8497;
    --sea-deep: #0f3a4c;
    --title-light: #e4dde6;
    --title-mid: #9a8fa3;
    --title-dark: #2a1d33;
    --artist: #ffffff;
  }
  * { margin: 0; padding: 0; box-sizing: border-box; }
  html, body {
    width: 1200px;
    height: 1200px;
    overflow: hidden;
    background: #ffffff;
  }
  .album-cover {
    position: relative;
    width: 1200px;
    height: 1200px;
    overflow: hidden;
  }
  .cover-artwork {
    position: absolute;
    inset: 0;
    background:
      radial-gradient(circle at 284px 205px, var(--sun) 0, rgba(255, 236, 150, 0.9) 90px, rgba(247, 166, 64, 0) 380px),
      linear-gradient(to bottom,
        rgba(0, 0, 0, 0) 0, rgba(0, 0, 0, 0) 470px,
        rgba(110, 90, 76, 0.85) 500px, rgba(110, 90, 76, 0.9) 700px,
        rgba(201, 178, 122, 0.9) 720px, rgba(255, 244, 190, 0.85) 790px,
        rgba(143, 195, 199, 0.9) 900px, rgba(46, 132, 151, 1) 1020px,
        var(--sea-deep) 1200px),
      linear-gradient(125deg, var(--amber) 0%, var(--ember) 35%, var(--dusk) 60%, var(--night) 85%);
  }
  .cover-title {
    position: absolute;
    inset: 0;
    font-family: "Uncial Antiqua", serif;
    font-weight: 400;
    line-height: 1;
    filter: drop-shadow(0 3px 4px rgba(30, 15, 35, 0.7));
  }
  .title-line {
    position: absolute;
    left: 0;
    right: 0;
    text-align: center;
    white-space: nowrap;
    background: linear-gradient(to bottom, var(--title-light) 0%, var(--title-mid) 45%, var(--title-dark) 55%, var(--title-light) 100%);
    -webkit-background-clip: text;
    background-clip: text;
    color: transparent;
  }
  .title-article {
    top: 306px;
    font-size: 104px;
    letter-spacing: -2px;
  }
  .title-main {
    top: 428px;
    font-size: 176px;
    letter-spacing: -4px;
  }
  .title-second {
    top: 712px;
    font-size: 146px;
    letter-spacing: -1px;
  }
  .artist-name {
    position: absolute;
    left: 0;
    right: 0;
    top: 1104px;
    text-align: center;
    font-family: "Josefin Sans", sans-serif;
    font-weight: 600;
    font-size: 29px;
    line-height: 1;
    letter-spacing: 22px;
    padding-left: 22px;
    color: var(--artist);
  }
</style>
</head>
<body>
  <main class="album-cover">
    <div class="cover-artwork" role="img" aria-label="Cover artwork area in warm sky and cool sea tones"></div>
    <h1 class="cover-title">
      <span class="title-line title-article">The</span>
      <span class="title-line title-main">Amber</span>
      <span class="title-line title-second">Tides</span>
    </h1>
    <p class="artist-name">OSKAR VENLOW</p>
  </main>
</body>
</html>
```